Need a Car Magnet designed

I need a car magnet designed.

The dimensions have to be 9" width by 2.6" height.

It needs to say BLORVIK TOUR and include the attached logo

```html
<!DOCTYPE html>
<html lang="en">
<head>
<meta charset="utf-8">
<title>BLORVIK TOUR Car Magnets</title>
<link rel="stylesheet" href="https://fonts.googleapis.com/css2?family=Cinzel:wght@900&display=swap">
<style>
  :root {
    --backdrop: #5b5b5b;
    --tour-blue: #1e4389;
    --tour-red: #d12f18;
    --panel-white: #ffffff;
  }
  html, body {
    margin: 0;
    padding: 0;
    width: 1200px;
    height: 825px;
    overflow: hidden;
    background: var(--backdrop);
  }
  .canvas {
    position: relative;
    width: 1200px;
    height: 825px;
  }
  .magnet {
    position: absolute;
    left: 118px;
    width: 964px;
    height: 278px;
    filter: drop-shadow(4px 5px 5px rgba(0, 0, 0, 0.45));
  }
  .magnet--blue { top: 106px; --accent: var(--tour-blue); }
  .magnet--red  { top: 446px; --accent: var(--tour-red); }
  .magnet__frame { fill: var(--accent); }
  .magnet__panel { fill: var(--panel-white); }
  .wordmark {
    font-family: "Cinzel", "Times New Roman", serif;
    font-weight: 900;
    font-size: 108px;
    fill: var(--accent);
  }
  .brand-name {
    font-family: "Cinzel", "Times New Roman", serif;
    font-weight: 900;
    font-size: 34px;
    fill: var(--tour-blue);
  }
  .brand-dot { fill: var(--tour-blue); }
</style>
</head>
<body>
<main class="canvas">

  <svg class="magnet magnet--blue" viewBox="0 0 964 278" aria-label="BLORVIK TOUR car magnet, blue">
    <rect class="magnet__frame" x="0" y="0" width="964" height="278"/>
    <rect class="magnet__panel" x="20" y="18" width="926" height="242" rx="14"/>
    <g class="brand-lockup">
      <circle class="brand-dot" cx="80" cy="134" r="34"/>
      <text class="brand-name" x="128" y="128">BLORVIK</text>
      <text class="brand-name" x="128" y="166">TOUR</text>
    </g>
    <text class="wordmark" x="330" y="148" textLength="540" lengthAdjust="spacingAndGlyphs" transform="rotate(-4 330 148)">BLORVIK</text>
    <text class="wordmark" x="494" y="246" textLength="430" lengthAdjust="spacingAndGlyphs" transform="rotate(-4.3 494 246)">TOUR</text>
  </svg>

  <svg class="magnet magnet--red" viewBox="0 0 964 278" aria-label="BLORVIK TOUR car magnet, red">
    <rect class="magnet__frame" x="0" y="0" width="964" height="278"/>
    <rect class="magnet__panel" x="20" y="18" width="926" height="242" rx="14"/>
    <g class="brand-lockup">
      <circle class="brand-dot" cx="80" cy="134" r="34"/>
      <text class="brand-name" x="128" y="128">BLORVIK</text>
      <text class="brand-name" x="128" y="166">TOUR</text>
    </g>
    <text class="wordmark" x="330" y="148" textLength="540" lengthAdjust="spacingAndGlyphs" transform="rotate(-4 330 148)">BLORVIK</text>
    <text class="wordmark" x="494" y="246" textLength="430" lengthAdjust="spacingAndGlyphs" transform="rotate(-4.3 494 246)">TOUR</text>
  </svg>

</main>
</body>
</html>
```